Artist needs a business card for her pencil portraits and streetscapes

My mum is an artist and does fabulous portraits and sketches with pencil and needs a business card.
She likes designs that are a bit weird or unusual. The winning design will NOT be a slick modern corporate looking logo. It should be a little bit rustic and different. Interesting patterns and textures would be great, it doesn't even need to look like a business card! Come up with something unique!

Target Market(s)

Older clientele looking for family portraits

Industry/Entity Type

Artists

Contact Information for Business Card

Basically just need the name and contact details

Font styles to use
Decorative
Script

Requirements
Must have
• Lena Brodsworth
• Artist
• 0427913562
• lenabrodsworth@quillpost.example
Nice to have
• Weird artistic backgrounds, interesting textures, unusual designs for an artistic woman.
Should not have
• Nothing ultra modern and nothing corporate looking.

```html
<!DOCTYPE html>
<html lang="en">
<head>
<meta charset="utf-8">
<title>Lena Brodsworth – Artist</title>
<link rel="stylesheet" href="https://fonts.googleapis.com/css2?family=Libre+Baskerville&display=swap">
<style>
  :root {
    --page-bg: #d9d6d0;
    --card-base: #3a3a3a;
    --card-dark: #222222;
    --card-light: #585858;
    --ink: #f2f2f2;
    --ink-soft: #d8d8d8;
    --rule: #e6e6e6;
  }
  * { margin: 0; padding: 0; box-sizing: border-box; }
  html, body {
    width: 1200px;
    height: 1022px;
    overflow: hidden;
    background: var(--page-bg);
  }
  .business-card {
    position: absolute;
    left: 180px;
    top: 271px;
    width: 840px;
    height: 480px;
    border-radius: 22px;
    overflow: hidden;
    background:
      radial-gradient(ellipse 260px 180px at 18% 35%, rgba(120,120,120,0.35), transparent 70%),
      radial-gradient(ellipse 240px 170px at 75% 70%, rgba(15,15,15,0.55), transparent 70%),
      radial-gradient(ellipse 300px 200px at 88% 20%, rgba(25,25,25,0.5), transparent 70%),
      radial-gradient(ellipse 180px 140px at 40% 85%, rgba(95,95,95,0.3), transparent 70%),
      linear-gradient(135deg, var(--card-light) 0%, var(--card-base) 40%, var(--card-dark) 100%);
    box-shadow: 0 18px 40px rgba(0,0,0,0.25);
    font-family: "Libre Baskerville", "Times New Roman", serif;
    color: var(--ink);
  }
  .card-texture {
    position: absolute;
    inset: 0;
    width: 100%;
    height: 100%;
    mix-blend-mode: overlay;
    opacity: 0.75;
  }
  .divider {
    position: absolute;
    left: 0;
    right: 0;
    top: 240px;
    height: 1.5px;
    background: var(--rule);
  }
  .name {
    position: absolute;
    left: 292px;
    top: 152px;
    font-size: 25px;
    font-weight: 400;
    letter-spacing: 0.4px;
    line-height: 1.2;
    white-space: nowrap;
  }
  .role {
    position: absolute;
    left: 410px;
    top: 186px;
    font-size: 15px;
    color: var(--ink-soft);
    white-space: nowrap;
  }
  .contact-icons {
    position: absolute;
    left: 402px;
    top: 220px;
    display: flex;
    gap: 16px;
  }
  .contact-icons svg { width: 14px; height: 14px; display: block; }
  .contact-details {
    position: absolute;
    left: 208px;
    width: 500px;
    top: 258px;
    text-align: center;
    color: var(--ink-soft);
    white-space: nowrap;
  }
  .contact-details .phone { font-size: 17px; letter-spacing: 0.8px; line-height: 28px; }
  .contact-details .email { font-size: 14px; letter-spacing: 1px; line-height: 34px; text-transform: uppercase; }
</style>
</head>
<body>
  <div class="business-card">
    <svg class="card-texture" viewBox="0 0 840 480" preserveAspectRatio="none" aria-hidden="true">
      <filter id="grunge" x="0" y="0" width="100%" height="100%">
        <feTurbulence type="fractalNoise" baseFrequency="0.035" numOctaves="5" seed="7"/>
        <feColorMatrix type="matrix" values="0 0 0 0 0.5  0 0 0 0 0.5  0 0 0 0 0.5  1.6 0 0 0 -0.55"/>
      </filter>
      <filter id="speckle" x="0" y="0" width="100%" height="100%">
        <feTurbulence type="fractalNoise" baseFrequency="0.9" numOctaves="2" seed="3"/>
        <feColorMatrix type="matrix" values="0 0 0 0 0  0 0 0 0 0  0 0 0 0 0  0 0 0 -2.2 1.25"/>
      </filter>
      <rect width="840" height="480" filter="url(#grunge)"/>
      <rect width="840" height="480" filter="url(#speckle)" opacity="0.5"/>
    </svg>
    <div class="divider"></div>
    <h1 class="name">Lena Brodsworth</h1>
    <p class="role">Artist</p>
    <div class="contact-icons">
      <svg viewBox="0 0 16 16" aria-label="phone" role="img">
        <path d="M4 1.5 L6 4.5 L4.8 6 C5.6 7.8 7.2 9.6 9.5 11 L11 9.8 L14 11.8 L12.5 14.5 C7 14 2 9 1.5 3.5 Z" fill="none" stroke="#f2f2f2" stroke-width="1.4" stroke-linejoin="round"/>
      </svg>
      <svg viewBox="0 0 16 16" aria-label="email" role="img">
        <rect x="1.5" y="3.5" width="13" height="9" fill="none" stroke="#f2f2f2" stroke-width="1.4"/>
        <path d="M1.5 3.5 L8 9 L14.5 3.5" fill="none" stroke="#f2f2f2" stroke-width="1.4"/>
      </svg>
    </div>
    <div class="contact-details">
      <p class="phone">0427913562</p>
      <p class="email">lenabrodsworth@quillpost.example</p>
    </div>
  </div>
</body>
</html>
```